GlowNest....... a touch of Bliss

I need a web design for a new business based in London that will be mobile (offered at homes, parks or a local cafe ect) called GlowNest. I offer Life Coaching/Counselling sessions, Personal training, Massage and Sports Massage. Sessions range from an hour to half and hour. My aim is to help people along their journey to help give them gain clarity of where there going, helping them to towards their goals, so that can experience bliss. My website should represent a place people can come to release their stress and worries so that they leave feeling lighter, clearer and happier. I would like my website to reflect someone feeling ALIVE. I would also like a logo design for GlowNest with a sentence underneath or near saying a touch of bliss.

Target Market(s)

middle class people

Industry/Entity Type

Business

Coding

Coded - Design and coding required

Number of Pages Required

4 page

Requirements
Must have
• 1st page About us
• 2nd page Services
• 3rd page Prices
• 4th page contact details
Nice to have
• mixture of cultures in images

```html
<!DOCTYPE html>
<html lang="en">
<head>
<meta charset="utf-8">
<title>GlowNest — a touch of bliss</title>
<link href="https://fonts.googleapis.com/css2?family=Lato:wght@300;400;700&family=Open+Sans:wght@300;700&family=Pacifico&display=swap" rel="stylesheet">
<style>
  :root {
    --sky-top: #5f97b8;
    --sky-mid: #86bccd;
    --reed-gold: #b88a4c;
    --reed-dark: #2a1d14;
    --white: #ffffff;
    --nav-text: rgba(255,255,255,0.85);
    --ink: #444444;
    --ink-soft: #8a8a8a;
    --icon: #6b6b6b;
    --chevron-bg: rgba(50,32,18,0.85);
  }
  * { margin: 0; padding: 0; box-sizing: border-box; }
  html, body { width: 1200px; height: 811px; overflow: hidden; background: var(--white); }
  body { position: relative; font-family: "Lato", sans-serif; }

  .hero {
    position: absolute; left: 0; top: 0; width: 1200px; height: 562px;
  }
  .hero-photo {
    position: absolute; inset: 0;
    background:
      linear-gradient(180deg, var(--sky-top) 0%, var(--sky-mid) 38%, rgba(0,0,0,0) 52%),
      linear-gradient(180deg, #9ab6a6 40%, var(--reed-gold) 62%, #7a5a34 82%, var(--reed-dark) 100%);
  }

  .site-header {
    position: absolute; left: 143px; right: 85px; top: 10px; height: 30px;
    display: flex; align-items: center; justify-content: space-between;
  }
  .brand {
    font-family: "Lato", sans-serif; font-weight: 700; font-size: 22px;
    color: rgba(225,235,242,0.9);
  }
  .main-nav { display: flex; gap: 28px; }
  .main-nav a {
    font-family: "Lato", sans-serif; font-weight: 300; font-size: 14.5px;
    color: var(--nav-text); text-decoration: none;
  }

  .hero-title {
    position: absolute; left: 0; right: 0; top: 182px; text-align: center;
    font-family: "Open Sans", sans-serif; font-weight: 700; font-size: 50px;
    color: rgba(255,255,255,0.95); line-height: 1;
  }
  .hero-tagline {
    position: absolute; left: 0; right: 0; top: 238px; text-align: center;
    font-family: "Pacifico", cursive; font-size: 27px;
    color: rgba(255,255,255,0.95); line-height: 1.2;
  }
  .cta {
    position: absolute; left: 493px; top: 318px; width: 209px; height: 70px;
    border: 2px solid rgba(255,255,255,0.9); border-radius: 2px;
    display: flex; align-items: center; justify-content: center;
    font-family: "Open Sans", sans-serif; font-weight: 300; font-size: 25px;
    color: var(--white); text-decoration: none;
  }
  .scroll-down {
    position: absolute; left: 573px; top: 451px; width: 54px; height: 54px;
    border-radius: 50%; background: var(--chevron-bg);
    display: flex; align-items: center; justify-content: center;
  }

  .services {
    position: absolute; left: 0; top: 562px; width: 1200px; height: 249px;
  }
  .service {
    position: absolute; top: 95px; width: 320px; text-align: center;
  }
  .service-icon {
    width: 88px; height: 88px; margin: 0 auto;
    border: 2px solid #4a4a4a; border-radius: 50%;
    display: flex; align-items: center; justify-content: center;
  }
  .service-title {
    margin-top: 6px;
    font-family: "Lato", sans-serif; font-weight: 400; font-size: 23px; color: var(--ink);
  }
  .service-text {
    margin-top: 14px;
    font-family: "Lato", sans-serif; font-weight: 300; font-size: 13px; color: var(--ink-soft);
  }
</style>
</head>
<body>
  <section class="hero">
    <div class="hero-photo" role="img" aria-label="Blurred photo of golden reeds under a clear blue sky"></div>

    <header class="site-header">
      <div class="brand">GlowNest</div>
      <nav class="main-nav">
        <a href="#coaching">Life Coaching/Counseling</a>
        <a href="#training">Personal Training</a>
        <a href="#massage">(Sports) Massage</a>
        <a href="#contact">Contact</a>
      </nav>
    </header>

    <h1 class="hero-title">GlowNest</h1>
    <p class="hero-tagline">a touch of bliss</p>
    <a class="cta" href="#services">Get Started</a>
    <a class="scroll-down" href="#services" aria-label="Scroll down">
      <svg width="16" height="12" viewBox="0 0 16 12"><path d="M2 3 L8 9 L14 3" fill="none" stroke="#fff" stroke-width="3" stroke-linecap="round" stroke-linejoin="round"/></svg>
    </a>
  </section>

  <section class="services" id="services">
    <article class="service" style="left:125px" id="coaching">
      <div class="service-icon">
        <svg width="32" height="26" viewBox="0 0 32 26" fill="#6b6b6b">
          <ellipse cx="12" cy="10" rx="11" ry="8"/>
          <path d="M5 15 L3 21 L10 17 Z"/>
          <ellipse cx="22" cy="15" rx="9" ry="6.5" stroke="#fff" stroke-width="1.5"/>
          <path d="M26 19 L29 24 L22 21 Z"/>
        </svg>
      </div>
      <h2 class="service-title">Life Coaching/ Counseling</h2>
      <p class="service-text">Look around joyful bounteous rainbow keenness</p>
    </article>

    <article class="service" style="left:440px" id="training">
      <div class="service-icon">
        <svg width="20" height="28" viewBox="0 0 20 28" fill="#6b6b6b">
          <circle cx="10" cy="4" r="3.5"/>
          <path d="M6 9 H14 V18 H12.5 V27 H10.8 V19 H9.2 V27 H7.5 V18 H6 Z"/>
          <path d="M6 9 L2 4 L3.5 3 L7 7 Z M14 9 L18 4 L16.5 3 L13 7 Z"/>
        </svg>
      </div>
      <h2 class="service-title">Personal Training</h2>
      <p class="service-text">Laugh juice friendly lenient vigor courteous joyful</p>
    </article>

    <article class="service" style="left:754px" id="massage">
      <div class="service-icon">
        <svg width="28" height="16" viewBox="0 0 28 16">
          <rect x="0" y="1" width="24" height="14" rx="1.5" fill="#6b6b6b"/>
          <rect x="24" y="5" width="3" height="6" fill="#6b6b6b"/>
          <path d="M13 3 L8 9 H12 L10 13 L16 7 H12 Z" fill="#fff"/>
        </svg>
      </div>
      <h2 class="service-title">(Sports) Massage</h2>
      <p class="service-text">Discover spirited fire going moonrise vivacity mild</p>
    </article>
  </section>
</body>
</html>
```